Basic Website for Vending Machine Business

We need a website designed for our vending machine business, Munchtronix, which is located in Ottawa, Canada. We requires a few links to standard sub-pages (About Us, Machines, Request a Machine, Report a Problem, Contact Us, etc.). We want it to be fun and simple. Possibly involve a vending machine in some way - make selections inside the machine the links to sub pages? Just an idea, we are very flexible though...please be creative. Attached are the drafts of our logo, we will provide the official copies of logo in near future. Key for our website is we want it visually appealing and fun, as opposed to formal.
Some slogans you may wish to use:
- Vend. Snack. Smile.
- Shop. Snack. Smile.
Target Market(s)
Small and medium size business owners.
Industry/Entity Type
Business

```html
<!DOCTYPE html>
<html lang="en">
<head>
<meta charset="utf-8">
<title>Munchtronix — Vend. Snack. Smile.</title>
<link href="https://fonts.googleapis.com/css2?family=Ubuntu:ital,wght@0,400;0,500;0,700;1,400&display=swap" rel="stylesheet">
<style>
:root{
  --orange:#d4621f;
  --orange-dark:#b44d12;
  --ink:#333333;
  --muted:#7a7a7a;
  --hero-dark:#1f1f1f;
  --hero-light:#5a5a5a;
  --footer:#2b2b2b;
  --footer-text:#8a8a8a;
  --rule:#e2e2e2;
}
*{margin:0;padding:0;box-sizing:border-box}
html,body{width:956px;height:1200px;overflow:hidden;background:#fff}
body{font-family:"Ubuntu",sans-serif;color:var(--ink);position:relative}
.page{position:relative;width:956px;height:1200px;border-top:2px solid var(--orange)}
.abs{position:absolute}

/* header */
.brand{left:78px;top:24px;display:flex;align-items:center;gap:6px;font-size:24px;font-weight:700;color:var(--orange)}
.brand-dot{width:16px;height:16px;border-radius:50%;background:var(--orange)}
.callus{left:682px;top:31px;display:flex;align-items:center;gap:5px;font-size:10px;font-weight:500}
.callus b{color:var(--orange);font-weight:500;font-size:11px}
.search{left:862px;top:30px;padding-left:12px;border-left:1px solid var(--rule)}

/* nav */
.nav{left:0;top:75px;width:956px;height:45px;background:linear-gradient(#e07a35,#c8591a);border-bottom:1px solid var(--orange-dark)}
.nav a{position:absolute;top:0;height:45px;line-height:45px;text-align:center;color:#fff;font-size:10px;text-decoration:none;border-right:1px solid var(--orange-dark)}
.nav a.active{background:#2f2f2f}

/* hero */
.hero{left:0;top:120px;width:956px;height:363px;background:linear-gradient(90deg,var(--hero-dark),#3c3c3c 45%,var(--hero-light))}
.hero h1{left:79px;top:82px;font-size:48px;font-weight:500;color:#fff;letter-spacing:-.5px}
.hero h1 .grey{color:#9a9a9a}
.hero h1 .hot{color:var(--orange)}
.hero p{left:80px;top:148px;width:420px;font-size:12px;line-height:17px;color:#b8b8b8}
.btn{left:78px;top:219px;width:90px;height:33px;line-height:33px;text-align:center;background:var(--orange);color:#fff;font-size:11px;font-weight:500;border-radius:3px}
.dots{left:79px;top:277px;display:flex;gap:3px}
.dots i{width:8px;height:8px;border-radius:50%;background:#777}
.dots i.on{background:var(--orange)}
.hero-machine{left:573px;top:32px;width:305px;height:310px;border-radius:4px;background:linear-gradient(160deg,#3a3a3a,#0d0d0d)}

/* welcome */
.framed{border:1px solid var(--rule);padding:4px;background:#fff}
.welcome-photo{left:78px;top:510px;width:202px;height:180px}
.fill{width:100%;height:100%}
.welcome-photo .fill{background:linear-gradient(135deg,#3c4a6a,#8a6040 70%,#c26040)}
h2{font-size:22px;font-weight:700;color:var(--ink)}
.welcome{left:306px;top:505px;width:305px}
.welcome p{font-size:10.5px;line-height:17px;color:var(--muted);margin-top:13px}
.welcome p+p{margin-top:17px}
.whatwedo{left:640px;top:505px;width:237px}
.whatwedo ul{list-style:none;margin-top:12px}
.whatwedo li{height:29px;line-height:29px;border-bottom:1px solid var(--rule);font-size:10.5px;display:flex;align-items:center;gap:8px}

/* news */
.news-title{left:78px;top:729px}
.card{top:780px;width:179px}
.card .framed{height:150px}
.card h3{font-size:14.5px;font-weight:400;color:var(--orange);margin-top:13px}
.card .meta{font-size:10.5px;margin-top:8px;padding-left:2px}
.card .meta b{font-weight:500}
.card .meta span{color:#999}
.card p{font-size:10px;line-height:16px;color:var(--muted);margin-top:5px}

/* footer */
.footer{left:0;top:1057px;width:956px;height:143px;background:var(--footer);border-bottom:2px solid var(--orange)}
.footer h4{position:absolute;top:29px;font-size:13.5px;font-weight:400;color:var(--orange)}
.f-line{position:absolute;font-size:8.5px;color:var(--footer-text);display:flex;align-items:center;gap:8px}
.social{left:419px;top:60px;display:flex;gap:5px}
.social i{width:15px;height:15px;border-radius:50%;background:#555}
.news-input{left:639px;top:54px;width:195px;height:30px;border:1px solid #555;border-radius:3px;background:#2b2b2b}
.go{left:838px;top:54px;width:40px;height:30px;line-height:30px;text-align:center;background:var(--orange);border-radius:3px;color:#fff;font-size:12px;font-weight:500}
.copy{right:78px;top:117px;font-size:8.5px;font-style:italic;color:#777}
</style>
</head>
<body>
<div class="page">

  <header>
    <div class="brand abs"><span class="brand-dot"></span>Munchtronix</div>
    <div class="callus abs">
      <svg width="18" height="13" viewBox="0 0 18 13"><path d="M1 4 Q9 -1 17 4 L15 6 L12 5 L12 3 Q9 2 6 3 L6 5 L3 6 Z" fill="#333"/><rect x="4" y="6" width="10" height="7" rx="1" fill="#333"/></svg>
      CALL US: <b>(000) 4120 9315</b>
    </div>
    <div class="search abs">
      <svg width="13" height="13" viewBox="0 0 13 13"><circle cx="5" cy="5" r="3.5" fill="none" stroke="#333" stroke-width="1.8"/><path d="M7.5 7.5 L12 12" stroke="#333" stroke-width="2.2"/></svg>
    </div>
  </header>

  <nav class="nav abs">
    <a class="active" style="left:78px;width:100px">HOME</a>
    <a style="left:178px;width:120px">ABOUT US</a>
    <a style="left:298px;width:122px">MACHINES</a>
    <a style="left:420px;width:156px">REQUEST A MACHINE</a>
    <a style="left:576px;width:165px">REPORT A PROBLEM</a>
    <a style="left:741px;width:136px">CONTACT US</a>
  </nav>

  <section class="hero abs">
    <h1 class="abs">Vend. <span class="grey">Snack.</span> <span class="hot">Smile</span></h1>
    <p class="abs">Sed ut perspiciatis unde omnis iste natus error sit voluptatem accusantium doloremque laudantium, totam rem aperiam, eaque ipsa quae ab illo inventore veritatis et quasi architecto beatae vitae dicta sunt explicabo.</p>
    <div class="btn abs">READ MORE</div>
    <div class="dots abs"><i></i><i></i><i class="on"></i><i></i></div>
    <div class="hero-machine abs" role="img" aria-label="Two glass-front drink vending machines stocked with bottles"></div>
  </section>

  <div class="welcome-photo framed abs"><div class="fill" role="img" aria-label="Customer choosing a drink at a row of vending machines"></div></div>

  <section class="welcome abs">
    <h2>Welcome!</h2>
    <p>Dolor nunc vule putateulr ips dol consec.Donec semp ertet laciniate ultricie upien disse comete dolo lectus fgilla itollicil tua ludin dolor nec met quam accumsan dolore condime netus lullam utlacus adipiscing ipsum molestie euismod .</p>
    <p>Dolor nunc vule putateulr ips dol consec.Donec semp ertet laciniate ultricie upien disse comete dolo lectus fgilla itollicil tua ludin dolor nec met quam .</p>
  </section>

  <section class="whatwedo abs">
    <h2>What We Do!</h2>
    <ul>
      <li><svg width="6" height="9"><path d="M1 1 L5 4.5 L1 8" fill="none" stroke="#d4621f" stroke-width="1.8"/></svg>Condimentum tellus tellus ed eget rutr</li>
      <li><svg width="6" height="9"><path d="M1 1 L5 4.5 L1 8" fill="none" stroke="#d4621f" stroke-width="1.8"/></svg>Fusce in sem sit amet dolor ultrices</li>
      <li><svg width="6" height="9"><path d="M1 1 L5 4.5 L1 8" fill="none" stroke="#d4621f" stroke-width="1.8"/></svg>Venenaincidunt tellus id euismod tell</li>
      <li><svg width="6" height="9"><path d="M1 1 L5 4.5 L1 8" fill="none" stroke="#d4621f" stroke-width="1.8"/></svg>Malesuada fames ac turpis leo eu mi</li>
      <li><svg width="6" height="9"><path d="M1 1 L5 4.5 L1 8" fill="none" stroke="#d4621f" stroke-width="1.8"/></svg>Antesqueaecenas consequat eleifen</li>
    </ul>
  </section>

  <h2 class="news-title abs">Latest News</h2>

  <article class="card abs" style="left:78px">
    <div class="framed"><div class="fill" role="img" aria-label="Woman looking at a vending machine" style="background:linear-gradient(90deg,#7a4a2a,#c48a50)"></div></div>
    <h3>Dolor nunc putateulr</h3>
    <div class="meta"><b>Feb 07 2015 |</b> <span>0 Comments</span></div>
    <p>Dolor nunc vule putateulr ips dol con sec.Donec semp ertet laciniate ultr.</p>
  </article>
  <article class="card abs" style="left:287px">
    <div class="framed"><div class="fill" role="img" aria-label="Row of red and white drink vending machines" style="background:linear-gradient(90deg,#c8242a,#d8d8e0 50%,#c8242a)"></div></div>
    <h3>Dolor nunc putateulr</h3>
    <div class="meta"><b>Feb 07 2015 |</b> <span>0 Comments</span></div>
    <p>Dolor nunc vule putateulr ips dol con sec.Donec semp ertet laciniate ultr.</p>
  </article>
  <article class="card abs" style="left:490px">
    <div class="framed"><div class="fill" role="img" aria-label="Black snack vending machine on a dark background" style="background:radial-gradient(circle,#3a3a3a,#111)"></div></div>
    <h3>Dolor nunc putateulr</h3>
    <div class="meta"><b>Feb 07 2015 |</b> <span>0 Comments</span></div>
    <p>Dolor nunc vule putateulr ips dol con sec.Donec semp ertet laciniate ultr.</p>
  </article>
  <article class="card abs" style="left:698px">
    <div class="framed"><div class="fill" role="img" aria-label="Ticket machines at a station with a route map above" style="background:linear-gradient(180deg,#d8d4c8,#c9a050 50%,#2a2a2a)"></div></div>
    <h3>Dolor nunc putateulr</h3>
    <div class="meta"><b>Feb 07 2015 |</b> <span>0 Comments</span></div>
    <p>Dolor nunc vule putateulr ips dol con sec.Donec semp ertet laciniate ultr.</p>
  </article>

  <footer class="footer abs">
    <h4 style="left:80px">Get In Touch</h4>
    <div class="f-line" style="left:80px;top:60px"><svg width="10" height="9"><path d="M0 5 L5 0 L10 5 L8.5 5 L8.5 9 L1.5 9 L1.5 5 Z" fill="#777"/></svg>Dummy Ottawa Street</div>
    <div class="f-line" style="left:80px;top:74px"><svg width="10" height="9"><path d="M0 3 Q5 0 10 3 L9 4.5 L1 4.5 Z" fill="#777"/><rect x="2" y="5" width="6" height="4" fill="#777"/></svg>800.555.0192</div>
    <div class="f-line" style="left:205px;top:60px"><svg width="10" height="9"><path d="M2 0 L4 0 L4.5 3 L3 4 Q4.5 6.5 6 7 L7 5.5 L10 6 L10 8.5 Q4 9.5 0.5 2 Z" fill="#777"/></svg>800.555.0147</div>
    <div class="f-line" style="left:205px;top:74px"><svg width="10" height="8"><rect width="10" height="8" fill="#777"/><path d="M0 0 L5 4.5 L10 0" fill="none" stroke="#2b2b2b"/></svg>info@munchtronix.com</div>

    <h4 style="left:420px">Follow Us!</h4>
    <div class="social abs"><i></i><i></i><i></i><i></i><i></i><i></i></div>

    <h4 style="left:640px">Newsletter Sign Up</h4>
    <div class="news-input abs"></div>
    <div class="go abs">GO</div>

    <div class="copy abs">Copyright © 2015 All Rights Reserved by Munchtronix.</div>
  </footer>

</div>
</body>
</html>
```